New business card/stationary for a consulting company

I am looking for a clean and very professional looking business card for my consulting company as well as corresponding stationary. I am uploading our logo. I like simple and powerful for the feel. No graphics but I am open on everything else. Below is my contact information but would like the final to be in a version I can add my employees information into and print. Thank you.

Daniel Whitcombe
dan@ferncrestadvisory.com
2738 North 17th Avenue, Summit Floor, Oak Brook, Illinois 60126
www.ferncrestadvisory.com

Industry/Entity Type

Consulting

Contact Information for Business Card

Daniel Whitcombe
dan@ferncrestadvisory.com
www.ferncrestadvisory.com

Font styles to use
Serif
Sans Serif

Requirements
Must have
• Our logo and the business card details.
Nice to have
• our website www.ferncrestadvisory.com

```html
<!DOCTYPE html>
<html lang="en">
<head>
<meta charset="utf-8">
<title>Ferncrest Advisory – Business Card</title>
<link rel="stylesheet" href="https://fonts.googleapis.com/css2?family=Lato:wght@400&display=swap">
<style>
  :root {
    --navy: #0b0b6e;
    --white: #ffffff;
    --ink: #1a1a1a;
    --backdrop: #2a2a2a;
  }
  * { margin: 0; padding: 0; box-sizing: border-box; }
  html, body {
    width: 1200px;
    height: 900px;
    overflow: hidden;
    background: var(--backdrop);
    font-family: "Lato", Arial, sans-serif;
  }
  .canvas {
    position: relative;
    width: 1200px;
    height: 900px;
  }
  .card {
    position: absolute;
    left: 250px;
    width: 700px;
    height: 400px;
    overflow: hidden;
  }
  .card--front { top: 40px; background: var(--navy); }
  .card--back  { top: 460px; background: var(--white); }

  .brand {
    position: absolute;
    display: flex;
    align-items: center;
    gap: 14px;
    letter-spacing: 3px;
    text-transform: uppercase;
    font-weight: 400;
    white-space: nowrap;
  }
  .brand__square {
    width: 26px;
    height: 26px;
  }
  .card--front .brand {
    left: 0; right: 0; top: 176px;
    justify-content: center;
    color: var(--white);
    font-size: 34px;
  }
  .card--front .brand__square { background: var(--white); }

  .card--back .brand {
    right: 60px; top: 66px;
    color: var(--navy);
    font-size: 28px;
  }
  .card--back .brand__square { width: 22px; height: 22px; background: var(--navy); }

  .holder {
    position: absolute;
    left: 56px;
    top: 168px;
    color: var(--navy);
    font-size: 30px;
    font-weight: 400;
    white-space: nowrap;
  }
  .holder-rule {
    position: absolute;
    left: 52px;
    top: 212px;
    width: 590px;
    height: 2px;
    background: var(--navy);
  }
  .contact {
    position: absolute;
    left: 52px;
    top: 252px;
    list-style: none;
    color: var(--ink);
    font-size: 19px;
    line-height: 30px;
    white-space: nowrap;
  }
  .contact li { display: flex; align-items: center; gap: 12px; }
  .contact svg { width: 20px; height: 16px; flex: none; }
  .address {
    position: absolute;
    right: 60px;
    top: 250px;
    text-align: right;
    font-style: normal;
    color: var(--ink);
    font-size: 19px;
    line-height: 28px;
    white-space: nowrap;
  }
  .edge-band {
    position: absolute;
    left: 0; right: 0; bottom: 0;
    height: 12px;
    background: var(--navy);
  }
</style>
</head>
<body>
<main class="canvas">

  <section class="card card--front" aria-label="Card front">
    <div class="brand">
      <span class="brand__square"></span>
      <span class="brand__name">Ferncrest Advisory</span>
    </div>
  </section>

  <section class="card card--back" aria-label="Card back">
    <div class="brand">
      <span class="brand__square"></span>
      <span class="brand__name">Ferncrest Advisory</span>
    </div>

    <h1 class="holder">Daniel Whitcombe</h1>
    <div class="holder-rule"></div>

    <ul class="contact">
      <li>
        <svg viewBox="0 0 20 16" aria-hidden="true">
          <rect x="1" y="2" width="18" height="12" fill="var(--navy)"/>
          <polyline points="1,2 10,9 19,2" fill="none" stroke="#fff" stroke-width="1.4"/>
        </svg>
        <span>dan@ferncrestadvisory.com</span>
      </li>
      <li>
        <svg viewBox="0 0 20 16" aria-hidden="true">
          <circle cx="10" cy="8" r="7" fill="var(--navy)"/>
          <g fill="none" stroke="#fff" stroke-width="1">
            <ellipse cx="10" cy="8" rx="3" ry="7"/>
            <line x1="3" y1="8" x2="17" y2="8"/>
            <line x1="10" y1="1" x2="10" y2="15"/>
          </g>
        </svg>
        <span>www.ferncrestadvisory.com</span>
      </li>
    </ul>

    <address class="address">
      2738 North 17th Avenue<br>
      Summit Floor<br>
      Westmoor Ridge, Ohio 43917
    </address>

    <div class="edge-band"></div>
  </section>

</main>
</body>
</html>
```